Disability provider requiring digital flyer to promote services

My company works within the Disability sector (QCWP registered provider), currently operating in Sydney, Australia.
I require a digital brochure which lists our services and gives potential customers a quick look into what we do with a single glance.
Undecided whether this digital flyer is to be single or double sided, happy to consult with an experienced designer in this regard.
I prefer minimalist designs (which may be an issue for someone trying to convey information, I'm not sure), and possibly someone who can work with out watercolor logo.
Services include:
-Supported Independent Living
-Specialist Disability Accommodation
-Individualised Living Options Stage 1 & 2
-Home Modifications
-Occupational Therapy
-Support Coordination Levels 1 & 2
-Short Term Accommodation - STA Respite
-Drop In Supports
-Community Access

```html
<!DOCTYPE html>
<html lang="en">
<head>
<meta charset="utf-8">
<title>QCWP Services Flyer – Lumenvale Care</title>
<link rel="stylesheet" href="https://fonts.googleapis.com/css2?family=Rubik:wght@500;600&display=swap">
<style>
  :root {
    --page: #e6e6e6;
    --band-light: #b3b3b3;
    --band-mid: #6b6b6b;
    --band-dark: #000000;
    --purple: #692b76;
    --white: #ffffff;
    --photo-light: #c9c9c9;
    --photo-dark: #5c5c5c;
  }
  * { margin: 0; padding: 0; box-sizing: border-box; }
  html, body {
    width: 1200px;
    height: 1200px;
    overflow: hidden;
    background: var(--page);
  }
  .flyer {
    position: absolute;
    left: 22px;
    top: 210px;
    width: 1156px;
    height: 779px;
    overflow: hidden;
  }
  .flyer svg { display: block; }
  .band-light { fill: var(--band-light); }
  .band-mid { fill: var(--band-mid); }
  .band-dark { fill: var(--band-dark); }
  .bubble { fill: var(--purple); }
  .service-label {
    font-family: "Rubik", sans-serif;
    font-weight: 500;
    font-size: 13.4px;
    fill: var(--white);
    text-anchor: middle;
  }
  .scheme-name {
    font-family: "Rubik", sans-serif;
    font-weight: 600;
    font-size: 74px;
    fill: var(--white);
    text-anchor: middle;
  }
  .brand-name {
    font-family: "Rubik", sans-serif;
    font-weight: 500;
    font-size: 27px;
    fill: var(--white);
    letter-spacing: 1px;
  }
</style>
</head>
<body>
<main class="flyer">
  <svg width="1156" height="779" viewBox="0 0 1156 779" xmlns="http://www.w3.org/2000/svg">
    <defs>
      <linearGradient id="photoTone" x1="0" y1="0" x2="0.6" y2="1">
        <stop offset="0" stop-color="var(--photo-light)"/>
        <stop offset="1" stop-color="var(--photo-dark)"/>
      </linearGradient>
    </defs>

    <!-- background bands -->
    <rect class="band-light" x="0" y="0" width="1156" height="260"/>
    <rect class="band-mid" x="0" y="260" width="1156" height="260"/>
    <rect class="band-dark" x="0" y="520" width="1156" height="259"/>

    <!-- athlete photo area -->
    <circle cx="864" cy="579" r="256" fill="url(#photoTone)" role="img"
            aria-label="Black and white photo of a wheelchair basketball player preparing to shoot"/>

    <!-- scheme badge -->
    <circle class="bubble" cx="188" cy="191" r="137"/>
    <text class="scheme-name" x="188" y="217">QCWP</text>

    <!-- service bubbles -->
    <g class="service">
      <circle class="bubble" cx="558" cy="191" r="69"/>
      <text class="service-label" x="558" y="187">HOME</text>
      <text class="service-label" x="558" y="206">MODIFICATIONS</text>
    </g>
    <g class="service">
      <circle class="bubble" cx="682" cy="113" r="69"/>
      <text class="service-label" x="682" y="100">SHORT TERM</text>
      <text class="service-label" x="682" y="118">ACCOMODATION</text>
      <text class="service-label" x="682" y="137">STA RESPITE</text>
    </g>
    <g class="service">
      <circle class="bubble" cx="823" cy="83" r="69"/>
      <text class="service-label" x="823" y="79">DROP IN</text>
      <text class="service-label" x="823" y="98">SUPPORTS</text>
    </g>
    <g class="service">
      <circle class="bubble" cx="967" cy="104" r="69"/>
      <text class="service-label" x="967" y="93">INDIVIDUALISED</text>
      <text class="service-label" x="967" y="111">LIVING OPTION</text>
      <text class="service-label" x="967" y="130">STAGE 1 AND 2</text>
    </g>
    <g class="service">
      <circle class="bubble" cx="1095" cy="171" r="69"/>
      <text class="service-label" x="1095" y="166">COMMUNITY</text>
      <text class="service-label" x="1095" y="185">ACCESS</text>
    </g>
    <g class="service">
      <circle class="bubble" cx="469" cy="304" r="69"/>
      <text class="service-label" x="469" y="292">SPECIALIST</text>
      <text class="service-label" x="469" y="310">DISABILITY</text>
      <text class="service-label" x="469" y="329">ACCOMODATION</text>
    </g>
    <g class="service">
      <circle class="bubble" cx="424" cy="443" r="69"/>
      <text class="service-label" x="424" y="430">SUPPORT</text>
      <text class="service-label" x="424" y="449">COORDINATION</text>
      <text class="service-label" x="424" y="467">LEVEL 1 AND 2</text>
    </g>
    <g class="service">
      <circle class="bubble" cx="429" cy="588" r="69"/>
      <text class="service-label" x="429" y="580">SUPPORTED</text>
      <text class="service-label" x="429" y="598">INDEPENDENT</text>
      <text class="service-label" x="429" y="617">LIVING</text>
    </g>
    <g class="service">
      <circle class="bubble" cx="484" cy="722" r="69"/>
      <text class="service-label" x="484" y="718">OCCUPATIONAL</text>
      <text class="service-label" x="484" y="737">THERAPY</text>
    </g>

    <!-- provider name -->
    <text class="brand-name" x="47" y="720">LUMENVALE CARE</text>
  </svg>
</main>
</body>
</html>
```